Business Card Design

The new Company is called The Harbor Pantry - based in Coral Bay, Florida and Connecticut. We want a business card to be catchy and memorable ( like our Company name). Our business is marketing and retail sales of flavored cashew nuts in boutique /high end stores. The new business card must include a logo which must be a cashew nut with a king's crown or Roman wreath.
Yes- we are looking for a logo to be designed for the business and for the business card.

Industry/Entity Type

Marketing

Font styles to use
Script

```html
<!DOCTYPE html>
<html lang="en">
<head>
<meta charset="utf-8">
<title>The Harbor Pantry — Business Card</title>
<link rel="stylesheet" href="https://fonts.googleapis.com/css2?family=Merienda:wght@700&family=Gelasio:ital,wght@0,400;0,700;1,400&display=swap">
<style>
  :root {
    --backdrop: #2a2a2c;
    --card-red: #7d1500;
    --brand-gold: #e3c06a;
    --text-white: #ffffff;
  }
  * { margin: 0; padding: 0; box-sizing: border-box; }
  html, body {
    width: 1200px; height: 900px; overflow: hidden;
    background: var(--backdrop);
  }
  .business-card {
    position: absolute;
    left: 150px; top: 193px;
    width: 900px; height: 514px;
    background: var(--card-red);
    color: var(--text-white);
    font-family: "Gelasio", Georgia, serif;
  }
  .brand-mark {
    position: absolute;
    left: 222px; top: 40px;
    width: 130px; height: 130px;
    border: 5px solid var(--brand-gold);
    border-radius: 50%;
  }
  .brand-name {
    position: absolute;
    left: 70px; top: 195px;
    font-family: "Merienda", cursive;
    font-weight: 700;
    font-size: 38px;
    color: var(--brand-gold);
    white-space: nowrap;
  }
  .holder {
    position: absolute;
    right: 40px; top: 64px;
    text-align: left;
  }
  .holder-name {
    font-weight: 700;
    font-size: 34px;
    line-height: 1;
  }
  .holder-role {
    font-style: italic;
    font-size: 22px;
    letter-spacing: 2px;
    margin-top: 2px;
  }
  .contact-block {
    position: absolute;
    font-size: 20px;
    line-height: 1.2;
  }
  .contact-label {
    font-weight: 700;
    font-size: 26px;
    margin-bottom: 8px;
  }
  .contact-address { left: 32px; top: 330px; }
  .contact-phone { left: 255px; top: 380px; text-align: center; }
  .contact-mail { right: 40px; top: 420px; text-align: center; }
</style>
</head>
<body>
  <section class="business-card">
    <div class="brand-mark"></div>
    <div class="brand-name">The Harbor Pantry</div>

    <div class="holder">
      <div class="holder-name">Daniel Reyes</div>
      <div class="holder-role">Director</div>
    </div>

    <div class="contact-block contact-address">
      <div class="contact-label">Address</div>
      <div>42, Palm Court Villa</div>
      <div>Coral Bay</div>
    </div>

    <div class="contact-block contact-phone">
      <div class="contact-label">Phone</div>
      <div>0198 765 432</div>
      <div>0198 765 432</div>
    </div>

    <div class="contact-block contact-mail">
      <div class="contact-label">Mail</div>
      <div>info@harborpantry.com</div>
      <div>www.harborpantry.com</div>
    </div>
  </section>
</body>
</html>
```